Helicopter company requires newspaper ad

"Ridgeline Aviation" is an agricultural helicopter company based in Victoria, Australia. We need an advert design for use in newspapers and also possibly social media. Our company specialises in using a helicopter for various agricultural work such as Spraying weeds ("Cropdusting"), spreading fertiliser. This advert will be targeted at farmers in our service area, Our customers are mainly dairy and cow farmers and our services are aimed at increasing their farm productivity. The final design should inform potential and existing customers about our services and the benefits of them. I will attach files of our logo and some existing advertising material for guidance. We would like the ad to feature the blue and green colours in our logo Please feel free to view our website and facebook page to see more about what we do. www.ridgelineaviation.com.au Some text we would like included Spraying: -Accurate -Time Efficient -Zero crop damage -Cost efficient Fertiliser Spreading: -Accurate, Pattern-tested equipment -Zero crop damage or wheel marks -Ability to load product out of a truck, bin or bulk bags -Cost effective, Prices from $32 per hectare depending on spread rate The final advert size should be 195 mm wide x 186 mm high Thanks :)

Farmers, Agriculture Industry

Agribusiness

Designer to choose colors to be used in the design.

• Phone number 0491 736 058
• The text included in the decription, or variations of this

```html
<!DOCTYPE html>
<html lang="en">
<head>
<meta charset="utf-8">
<title>Ridgeline Aviation – Summer Crops Ad</title>
<link rel="stylesheet" href="https://fonts.googleapis.com/css2?family=Archivo+Black&family=PT+Sans+Narrow:wght@400;700&family=Marcellus+SC&family=Marcellus&display=swap">
<style>
  :root {
    --sky-top: #1f5fd6;
    --sky-mid: #4f8ee8;
    --sky-low: #a9c8ee;
    --hill-light: #7fae4a;
    --hill-dark: #3f7a2c;
    --panel: rgba(235, 240, 250, 0.62);
    --ink: #111111;
    --white: #ffffff;
    --brand-blue: #1b6fd1;
  }
  html, body {
    margin: 0;
    padding: 0;
    overflow: hidden;
  }
  .ad {
    position: relative;
    width: 1200px;
    height: 1145px;
    overflow: hidden;
    font-family: "PT Sans Narrow", sans-serif;
  }
  .scene {
    position: absolute;
    inset: 0;
    background:
      linear-gradient(180deg,
        var(--sky-top) 0%,
        var(--sky-mid) 35%,
        var(--sky-low) 64%,
        var(--hill-light) 70%,
        var(--hill-dark) 86%,
        var(--hill-light) 100%);
  }
  .headline {
    position: absolute;
    left: 84px;
    top: 28px;
    margin: 0;
    font-family: "Archivo Black", sans-serif;
    font-weight: 400;
    font-size: 60px;
    line-height: 76px;
    letter-spacing: 3px;
    color: var(--white);
  }
  .panel {
    position: absolute;
    left: 670px;
    top: 207px;
    width: 455px;
    height: 938px;
    background: var(--panel);
  }
  .service {
    position: absolute;
    left: 30px;
    right: 20px;
    margin: 0;
  }
  .service--spraying { top: 34px; }
  .service--spreading { top: 274px; }
  .service h2 {
    margin: 0 0 10px;
    font-size: 28px;
    font-weight: 700;
    color: var(--ink);
    letter-spacing: 0.3px;
  }
  .service ul {
    list-style: none;
    margin: 0;
    padding: 0;
  }
  .service li {
    position: relative;
    padding-left: 38px;
    font-size: 29px;
    line-height: 39px;
    color: var(--ink);
  }
  .service li::before {
    content: "";
    position: absolute;
    left: 2px;
    top: 10px;
    width: 19px;
    height: 19px;
    border-radius: 50%;
    background: var(--ink);
  }
  .brand-box {
    position: absolute;
    left: 37px;
    top: 611px;
    width: 381px;
    height: 257px;
    background: var(--white);
    display: flex;
    align-items: center;
    justify-content: center;
    gap: 14px;
  }
  .brand-dot {
    width: 30px;
    height: 30px;
    border-radius: 50%;
    background: var(--brand-blue);
  }
  .brand-name {
    font-family: "PT Sans Narrow", sans-serif;
    font-weight: 700;
    font-size: 50px;
    color: var(--brand-blue);
  }
  .contact {
    position: absolute;
    left: 60px;
    top: 948px;
    width: 440px;
    text-align: center;
    color: var(--white);
    font-family: "Marcellus", serif;
  }
  .contact p { margin: 0; }
  .contact .tagline-top {
    font-family: "Marcellus SC", serif;
    font-size: 30px;
    line-height: 40px;
    letter-spacing: 1px;
  }
  .contact .tagline {
    font-size: 29px;
    line-height: 44px;
    letter-spacing: 0.5px;
  }
  .contact .phone {
    font-size: 28px;
    line-height: 38px;
    display: flex;
    justify-content: center;
    align-items: center;
    gap: 8px;
    letter-spacing: 1px;
  }
  .contact .web {
    font-size: 28px;
    line-height: 44px;
  }
</style>
</head>
<body>
<div class="ad">
  <div class="scene" role="img" aria-label="Photo of a helicopter over green rolling hills, spreading fertiliser from a slung bucket under a blue sky"></div>

  <h1 class="headline">Summer Crops Need<br>Spraying or Fertiliser?</h1>

  <aside class="panel">
    <section class="service service--spraying">
      <h2>SPRAYING:</h2>
      <ul>
        <li>Accurate</li>
        <li>Time efficient</li>
        <li>Zero crop damage</li>
        <li>Cost-effective</li>
      </ul>
    </section>
    <section class="service service--spreading">
      <h2>SPREADING:</h2>
      <ul>
        <li>Accurate, Pattern-tested equipment</li>
        <li>Zero crop damage or wheel marks</li>
        <li>Ability to load out of a Truck, Bin or bulk-bags</li>
        <li>Competitive Prices (from $32 per hectare depending on spread rate)</li>
      </ul>
    </section>
    <div class="brand-box">
      <span class="brand-dot"></span>
      <span class="brand-name">Ridgeline Aviation</span>
    </div>
  </aside>

  <footer class="contact">
    <p class="tagline-top">Owner/Operated</p>
    <p class="tagline">Aerial Agriculture Specialists</p>
    <p class="phone">
      <svg width="26" height="26" viewBox="0 0 26 26" aria-hidden="true">
        <circle cx="13" cy="13" r="11.5" fill="none" stroke="#fff" stroke-width="1.6"/>
        <path d="M9 7 q-2 1 -1 5 q2 5 6 7 q3 1 4 -1 l-2 -2 l-2 1 q-3 -2 -4 -5 l1 -2 z" fill="none" stroke="#fff" stroke-width="1.4" stroke-linejoin="round"/>
      </svg>
      0491 736 058
    </p>
    <p class="web">www.ridgelineaviation.com.au</p>
  </footer>
</div>
</body>
</html>
```